Book Cover Design for Millennial

I need a book cover design for my book Harbor Ascent. The subtitle of the book is How to Own, Enjoy and Excel in Your Career.

I'm a career coach who helps millennial career professionals. I myself am a millennial but on the older end (34). I've dealt and been through most of the challenges millennials are facing as career professionals and I wrote this book with the thought of providing guidance and aid to getting past those challenges and shedding light on fundamental habits and practices that will help them excel in their careers. In addition, the book will help them prepare millennials for our turn as the leaders, managers, etc moving forward in corporate America. The final design should have the main title of the book in it as the focal point but not the subtitle. I want the cover to communicate something NEW, Bold, Youthful, non-traditional. I want it to stick out while still maintaining a sleek and Professional look.
Updates

Hello, Designers! I want to thank you all for your submissions! The work is amazing and I greatly appreciate it. If you would I want to help out in this process by adding a few updates based on the submissions I have seen. The concept I think that is coming close to hitting the mark is Tessel Works. What I would like to see changed about the concept is the following: Change the outfits to be more Millennial Career Professional. I have attached some ideas to the brief. I want to replace this picture with one of multiple millennials anywhere from 3 and up. I would like the pic to have diversity in it representing most races of people in the USA. I would like my name beneath harbor ascent. I'm not a known author yet so having my name that big my distract from the title of the book. Can we make the title a little bigger and so far I like the background.Thanks, DW Added Friday, September 30, 2016

Target Market(s)

Millennial Career Professionals (18 - 34 age group)

Industry/Entity Type

Life Coaching

Logo Text

Harbor Ascent

Requirements
Must have
• communicate something NEW, Bold, Youthful, non-traditional. I want it to stick out while still maintaining a sleek and Professional look.
Nice to have
• something that goes with my brand
• http://www.darnellwhitby-example.com
Should not have
• Nothing 3D or a logo that is hard to read when placed on stationeries, business cards etc

```html
<!DOCTYPE html>
<html lang="en">
<head>
<meta charset="utf-8">
<title>Harbor Ascent – Book Cover</title>
<link href="https://fonts.googleapis.com/css2?family=Alfa+Slab+One&family=Oswald:wght@300;400;600;700&family=Montserrat:ital,wght@0,400;0,600;0,800;1,800&family=Bebas+Neue&display=swap" rel="stylesheet">
<style>
  :root {
    --ink: #0b0b0b;
    --paper: #ffffff;
    --accent-blue: #1f6fe8;
    --sun-yellow: #fdc83a;
    --sun-orange: #f7891c;
    --deep-orange: #f15a1e;
    --frame-grey: #3a3a3a;
    --title-black: #141414;
  }
  * { margin: 0; padding: 0; box-sizing: border-box; }
  html, body {
    width: 1200px; height: 903px; overflow: hidden; background: var(--ink);
  }
  .cover {
    position: relative; width: 1200px; height: 903px; background: var(--ink);
    color: var(--paper); font-family: "Montserrat", sans-serif;
  }

  /* Back cover */
  .back { position: absolute; left: 0; top: 0; width: 585px; height: 903px; background: var(--ink); }
  .back-title {
    position: absolute; left: 48px; top: 36px; width: 496px;
    font-family: "Oswald", sans-serif; font-weight: 700; font-size: 62px; line-height: 1;
    color: var(--accent-blue); letter-spacing: 3px; text-align: center; text-transform: uppercase;
  }
  .back-subtitle {
    position: absolute; left: 48px; top: 98px; width: 496px; text-align: center;
    font-family: "Montserrat", sans-serif; font-weight: 800; font-style: italic; font-size: 11px;
    color: var(--accent-blue); text-transform: uppercase;
  }
  .blurb {
    position: absolute; left: 48px; top: 141px; width: 496px;
    font-size: 13px; line-height: 17.6px; text-align: justify; height: 247px; overflow: hidden;
  }
  .author-portrait {
    position: absolute; left: 47px; top: 451px; width: 163px; height: 188px;
    border: 1px solid var(--frame-grey); background: var(--ink);
  }
  .about-heading {
    position: absolute; left: 243px; top: 450px; font-weight: 600; font-size: 14px;
  }
  .about-text {
    position: absolute; left: 243px; top: 477px; width: 305px;
    font-size: 13px; line-height: 17.8px; text-align: justify;
  }
  .isbn-block {
    position: absolute; left: 50px; top: 801px; width: 111px; height: 62px; background: var(--paper);
  }

  /* Spine */
  .spine { position: absolute; left: 585px; top: 0; width: 30px; height: 903px; background: var(--ink); }
  .spine-title {
    position: absolute; left: 2px; top: 44px; writing-mode: vertical-rl;
    font-family: "Oswald", sans-serif; font-weight: 700; font-size: 24px; letter-spacing: 6px;
    text-transform: uppercase; line-height: 26px;
  }
  .spine-author {
    position: absolute; left: 2px; top: 630px; writing-mode: vertical-rl;
    font-family: "Oswald", sans-serif; font-weight: 300; font-size: 24px; letter-spacing: 3px;
    text-transform: uppercase; line-height: 26px;
  }

  /* Front cover */
  .front {
    position: absolute; left: 615px; top: 0; width: 585px; height: 903px;
    background: linear-gradient(90deg, #f9a51f 0%, var(--sun-yellow) 35%, #fbb12a 60%, var(--sun-orange) 82%, var(--deep-orange) 100%);
  }
  .front-title {
    position: absolute; left: 0; top: 30px; width: 585px; text-align: center;
    font-family: "Alfa Slab One", serif; font-size: 128px; line-height: 106px;
    color: var(--title-black); text-transform: uppercase; letter-spacing: 4px;
    transform: scaleX(0.72); transform-origin: center top;
  }
  .front-subtitle {
    position: absolute; left: 0; top: 264px; width: 585px; text-align: center;
    font-family: "Oswald", sans-serif; font-weight: 700; font-size: 23px; letter-spacing: 0.5px;
    color: var(--title-black); text-transform: uppercase;
  }
  .team-photo {
    position: absolute; left: 0; top: 345px; width: 585px; height: 420px;
    background:
      radial-gradient(ellipse 60% 55% at 50% 70%, rgba(40,40,45,0.85), rgba(40,40,45,0) 70%),
      linear-gradient(180deg, rgba(0,0,0,0) 0%, rgba(60,55,55,0.55) 45%, rgba(35,35,40,0.9) 100%);
  }
  .author-band {
    position: absolute; left: 0; top: 765px; width: 585px; height: 138px; background: var(--ink);
  }
  .front-author {
    position: absolute; left: 0; top: 30px; width: 585px; text-align: center;
    font-family: "Bebas Neue", sans-serif; font-size: 86px; line-height: 84px; letter-spacing: 1px;
    color: var(--paper);
  }
</style>
</head>
<body>
<div class="cover">
  <section class="back">
    <h2 class="back-title">Harbor Ascent</h2>
    <p class="back-subtitle">How to enjoy, own and excel in your career.</p>
    <p class="blurb">Lorem Ipsum is simply dummy text of the printing and typesetting industry. Lorem Ipsum has been the industry's standard dummy text ever since the 1500s, when an unknown printer took a galley of type and scrambled it to make a type specimen book. It has survived not only five centuries, but also the leap into electronic typesetting, remaining essentially unchanged. It was popularised in the 1960s with the release of Quillsheet sheets containing Lorem Ipsum passages, and more recently with desktop publishing software like Pagecraft Studio including versions of Lorem Ipsum. Lorem Ipsum is simply dummy text of the printing and typesetting industry. Lorem Ipsum has been the industry's standard dummy text ever since the 1500s, when an unknown printer took a galley of type and scrambled it to make a type specimen book. It has survived not only five centuries, but also the leap into electronic typesetting, remaining essentially</p>
    <div class="author-portrait" role="img" aria-label="Author portrait placeholder"></div>
    <h3 class="about-heading">ABOUT AUTHOR</h3>
    <p class="about-text">Lorem Ipsum is simply dummy text of the printing and typesetting industry. Lorem Ipsum has been the industry's standard dummy text ever since the 1500s, when an unknown printer took a galley of type and scrambled it to make a type specimen book. It has survived not only five centuries, but also the leap into electronic typesetting, remaining essentially</p>
    <div class="isbn-block"></div>
  </section>

  <section class="spine">
    <span class="spine-title">Harbor Ascent</span>
    <span class="spine-author">Darnell Whitby</span>
  </section>

  <section class="front">
    <h1 class="front-title">Harbor<br>Ascent</h1>
    <p class="front-subtitle">How to enjoy, own and excel in your career.</p>
    <div class="team-photo" role="img" aria-label="Photograph of a diverse group of young professionals in business attire"></div>
    <div class="author-band">
      <p class="front-author">DARNELL WHITBY</p>
    </div>
  </section>
</div>
</body>
</html>
```